Brisk Framing website

I need a website for my construction. I want customers to see past builds and current projects Something that stands out and reflects awareness, safety, attention to details. I already have a logo designed by Pixel Harbor
Target Market(s)
Residential and Commercial sectors
Industry/Entity Type
Construction
Logo Text
Brisk Framing
Colors
EB3D1F
EC4F4E
F09395
F8D3D4
FCEDEE
Requirements
Must have
- My contact info
Nice to have
- Past projects

```html
<!DOCTYPE html>
<html lang="en">
<head>
<meta charset="utf-8">
<title>Brisk Framing</title>
<link href="https://fonts.googleapis.com/css2?family=Rajdhani:wght@500;600;700&family=Arimo:ital,wght@0,400;0,700;1,400&display=swap" rel="stylesheet">
<style>
:root{
  --brand:#eb3d1f;
  --brand-soft:#ec4f4e;
  --pink:#f09395;
  --ink:#2b2b2b;
  --text:#555;
  --muted:#8a8a8a;
  --light:#f5f5f5;
  --white:#fff;
}
*{margin:0;padding:0;box-sizing:border-box}
html,body{width:1200px;height:4113px;overflow:hidden}
body{position:relative;background:var(--white);font-family:"Arimo",Arial,sans-serif;color:var(--text)}
.abs{position:absolute}
.topline{left:0;top:0;width:640px;height:4px;background:var(--brand)}
.topline-gray{left:648px;top:0;width:552px;height:4px;background:#777}
.logo{left:112px;top:36px;font-family:"Rajdhani",sans-serif;font-weight:700;font-size:34px;color:var(--brand);letter-spacing:1px;display:flex;align-items:center;gap:10px}
.logo i{display:block;width:22px;height:22px;background:var(--brand)}
.nav{top:56px;font-family:"Rajdhani",sans-serif;font-weight:600;font-size:15px;color:var(--ink)}
.nav.active{color:var(--brand)}
.nav-sep{left:893px;top:52px;width:1px;height:26px;background:#ccc}
.quote-btn{left:940px;top:43px;width:150px;height:45px;background:var(--brand);color:#fff;font-family:"Rajdhani",sans-serif;font-weight:600;font-size:18px;display:flex;align-items:center;justify-content:center}
.hero-band{left:0;top:740px;width:1200px;height:100px;background:var(--brand);clip-path:polygon(0 0,100% 0,100% 10%,50% 95%,0 10%)}
.hero{left:0;top:120px;width:1200px;height:700px;background:linear-gradient(180deg,#3d78c4 0%,#7fa8d8 35%,#9a9ca3 62%,#6b5a4e 85%,#5a4a40 100%);clip-path:polygon(0 0,100% 0,100% 89%,50% 100%,0 89%)}
.hero-title{left:0;top:352px;width:1200px;text-align:center;font-family:"Rajdhani",sans-serif;font-weight:700;font-size:64px;color:#fff}
.hero-sub{left:0;top:438px;width:1200px;text-align:center;font-family:"Rajdhani",sans-serif;font-weight:600;font-size:23px;color:#fff}
.hero-btn{left:520px;top:493px;width:160px;height:59px;background:var(--brand);color:#fff;font-family:"Rajdhani",sans-serif;font-weight:700;font-size:19px;display:flex;align-items:center;justify-content:center}
.dot{top:782px;width:12px;height:12px;border-radius:50%;background:#fff}
.about-bg{left:0;top:1200px;width:1200px;height:324px;background:linear-gradient(180deg,#fff 0%,#ececec 100%)}
.about-frame{left:85px;top:1022px;width:200px;height:298px;border:9px solid #d9d9d9}
.about-photo{left:195px;top:905px;width:409px;height:532px;background:linear-gradient(160deg,#b9c6cf 0%,#c79b4c 40%,#6b8aa8 70%,#5a4a3c 100%)}
.eyebrow{font-family:"Rajdhani",sans-serif;font-weight:600;font-size:22px;color:var(--ink)}
.title{font-family:"Rajdhani",sans-serif;font-weight:700;font-size:48px;color:var(--brand);line-height:1}
.rule{height:2px;background:var(--brand)}
.copy{font-size:13.5px;line-height:26px;color:var(--text);text-align:justify}
.outline-btn{border:2px solid var(--brand);color:var(--ink);font-family:"Rajdhani",sans-serif;font-weight:600;font-size:18px;display:flex;align-items:center;justify-content:center;gap:12px}
.cta{left:0;top:1524px;width:1200px;height:156px;background:var(--brand)}
.cta-text{left:282px;top:1568px;font-family:"Rajdhani",sans-serif;font-weight:600;font-size:26px;line-height:36px;color:#fff}
.cta-btn{left:827px;top:1575px;width:192px;height:57px;border:2px solid #fff;color:#fff;font-family:"Rajdhani",sans-serif;font-weight:700;font-size:16px;display:flex;align-items:center;justify-content:center}
.why-photo{left:584px;top:1680px;width:616px;height:583px;background:linear-gradient(180deg,#4f86c6 0%,#9dbfe2 45%,#8b7f6f 75%,#5b4a3d 100%)}
.ring{width:110px;height:110px;border:3px solid var(--brand);border-radius:50%;display:flex;align-items:center;justify-content:center}
.feat-title{font-family:"Rajdhani",sans-serif;font-weight:600;font-size:23px;color:var(--ink)}
.feat-copy{font-size:13px;line-height:25px;color:var(--muted);width:300px}
.testi-bg{left:0;top:2263px;width:1200px;height:594px;background:var(--light)}
.center{left:0;width:1200px;text-align:center}
.card{width:313px;height:290px;background:#fff;box-shadow:0 2px 6px rgba(0,0,0,.12)}
.card::after{content:"";position:absolute;left:58px;bottom:-9px;width:18px;height:18px;background:#fff;transform:rotate(45deg);box-shadow:3px 3px 4px rgba(0,0,0,.08)}
.card .mark{position:absolute;left:20px;top:42px;font-family:Georgia,serif;font-weight:700;font-size:40px;line-height:30px;color:#666}
.card .stars{position:absolute;left:54px;top:44px;color:var(--brand);font-size:15px;letter-spacing:2px}
.card p{position:absolute;left:20px;top:82px;width:275px;font-style:italic;font-size:13px;line-height:23px;color:var(--muted)}
.avatar{width:64px;height:64px;border-radius:50%;background:linear-gradient(160deg,#c9b6a5,#6e5646);border:3px solid #fff;box-shadow:0 1px 4px rgba(0,0,0,.2)}
.author{font-family:"Rajdhani",sans-serif;font-weight:600;font-size:17px;color:var(--brand);line-height:22px}
.author span{display:block;font-family:"Arimo",sans-serif;font-weight:400;font-size:13px;color:var(--muted)}
.proj{background:linear-gradient(160deg,#8fb3d6,#c9b28a 60%,#4e3f33)}
.proj-overlay{font-family:"Rajdhani",sans-serif;color:#fff}
.footer{left:0;top:3600px;width:1200px;height:513px;background:var(--brand);clip-path:polygon(0 40px,50% 0,100% 40px,100% 100%,0 100%)}
.fnav{top:3673px;font-family:"Rajdhani",sans-serif;font-weight:700;font-size:17px;color:#fff}
.fline{left:112px;width:978px;height:1px;background:rgba(255,255,255,.35)}
.fhead{font-family:"Rajdhani",sans-serif;font-weight:700;font-size:25px;color:#fff}
.field{background:#fff;height:34px;font-size:11px;color:#555;padding:10px 12px}
.submit{left:112px;top:3976px;width:98px;height:32px;background:#3a3a3a;color:#fff;font-size:12px;display:flex;align-items:center;justify-content:center}
.ficon{width:44px;height:44px;border:2px solid #fff;border-radius:50%;display:flex;align-items:center;justify-content:center}
.finfo{font-family:"Rajdhani",sans-serif;color:#fff;font-weight:600;font-size:16px;line-height:20px}
.finfo span{display:block;font-size:12px;font-weight:500}
.flogo{left:832px;top:3818px;font-family:"Rajdhani",sans-serif;font-weight:700;font-size:36px;color:#fff;letter-spacing:1px}
.social{top:3898px;width:34px;height:34px;border:2px solid #fff;border-radius:50%}
.copyright{top:4060px;font-family:"Rajdhani",sans-serif;font-weight:500;font-size:15px;color:#fff}
</style>
</head>
<body>
<header>
  <div class="abs topline"></div><div class="abs topline-gray"></div>
  <div class="abs logo"><i></i>BRISK FRAMING</div>
  <nav>
    <span class="abs nav active" style="left:430px">HOME</span>
    <span class="abs nav" style="left:513px">SERVICES</span>
    <span class="abs nav" style="left:621px">PROJECTS</span>
    <span class="abs nav" style="left:734px">NEWS</span>
    <span class="abs nav" style="left:816px">CONTACT</span>
  </nav>
  <div class="abs nav-sep"></div>
  <svg class="abs" style="left:908px;top:56px" width="16" height="16" viewBox="0 0 16 16"><circle cx="6.5" cy="6.5" r="4.5" fill="none" stroke="#eb3d1f" stroke-width="2.2"/><line x1="10" y1="10" x2="14" y2="14" stroke="#eb3d1f" stroke-width="2.4"/></svg>
  <div class="abs quote-btn">GET A QUOTE</div>
</header>

<section class="hero-section">
  <div class="abs hero-band"></div>
  <div class="abs hero" role="img" aria-label="Tower cranes over concrete apartment blocks under construction against a blue sky"></div>
  <h1 class="abs hero-title">BRISK FRAMING</h1>
  <p class="abs hero-sub">SED UT PERSPICIATIS UNDE OMNIS ISTE NATUS ERROR SIT VOLUPTATEM</p>
  <div class="abs hero-btn">READ MORE</div>
  <span class="abs dot" style="left:575px"></span>
  <span class="abs dot" style="left:594px;background:var(--brand)"></span>
  <span class="abs dot" style="left:613px"></span>
</section>

<section class="about">
  <div class="abs about-bg"></div>
  <div class="abs about-frame"></div>
  <div class="abs about-photo" role="img" aria-label="Two workers in yellow hard hats tying steel reinforcement on site"></div>
  <div class="abs eyebrow" style="left:672px;top:920px">WELCOME</div>
  <h2 class="abs title" style="left:672px;top:955px">BRISK FRAMING</h2>
  <div class="abs rule" style="left:672px;top:1016px;width:268px"></div>
  <p class="abs copy" style="left:674px;top:1050px;width:398px">Sed ut perspiciatis unde omnis iste natus error sit voluptatem accusantium doloremque laudantium, totam rem aperiam, eaque ipsa quae ab illo inventore veritatis et quasi architecto beatae vitae dicta sunt explicabo. Nemo enim ipsam voluptatem quia voluptas sit aspernatur aut odit aut fugit, sed quia consequuntur magni dolores eos qui ratione voluptatem sequi nesciunt.</p>
  <p class="abs copy" style="left:674px;top:1232px;width:398px">Nemo enim ipsam voluptatem quia voluptas sit aspernatur aut odit aut fugit, sed quia consequuntur magni dolores eos qui ratione dolorem ipsum quia dolor sit amet, consectetur...</p>
  <div class="abs outline-btn" style="left:677px;top:1338px;width:181px;height:54px">READ MORE
    <svg width="32" height="10" viewBox="0 0 32 10"><line x1="0" y1="5" x2="29" y2="5" stroke="#2b2b2b" stroke-width="1.5"/><path d="M25 1 L31 5 L25 9" fill="none" stroke="#2b2b2b" stroke-width="1.5"/></svg>
  </div>
</section>

<section class="cta-band">
  <div class="abs cta"></div>
  <svg class="abs" style="left:174px;top:1562px" width="74" height="74" viewBox="0 0 74 74" fill="none" stroke="#fff" stroke-width="2.5"><path d="M4 30 L37 8 L70 30 V70 H4 Z"/><path d="M4 30 L37 52 L70 30"/><path d="M4 70 L30 47 M70 70 L44 47"/><rect x="16" y="16" width="30" height="22" fill="#eb3d1f"/><line x1="21" y1="24" x2="41" y2="24"/><line x1="21" y1="31" x2="36" y2="31"/><circle cx="56" cy="20" r="8" fill="#eb3d1f"/></svg>
  <p class="abs cta-text">LOOKING FOR A QUALITY CONSTRUCTION<br>FOR YOUR PROJECT?</p>
  <div class="abs cta-btn">GET A FREE QUOTE</div>
</section>

<section class="why">
  <div class="abs eyebrow" style="left:112px;top:1757px;font-size:21px">BRISK FRAMING</div>
  <h2 class="abs title" style="left:112px;top:1790px">WHY CHOOSE US</h2>
  <div class="abs rule" style="left:112px;top:1851px;width:220px"></div>
  <p class="abs copy" style="left:112px;top:1878px;width:430px;font-size:13px">Sed ut perspiciatis unde omnis iste natus error sit voluptatem accu santium doloremque laudantium, totam rem aperiam</p>
  <div class="abs ring" style="left:110px;top:1957px">
    <svg width="58" height="58" viewBox="0 0 58 58" fill="none" stroke="#eb3d1f" stroke-width="2"><path d="M29 12 L44 26 H38 V44 H20 V26 H14 Z"/><line x1="29" y1="2" x2="29" y2="8"/><line x1="6" y1="26" x2="11" y2="26"/><line x1="47" y1="26" x2="52" y2="26"/><line x1="12" y1="10" x2="16" y2="14"/><line x1="46" y1="10" x2="42" y2="14"/><circle cx="29" cy="32" r="4"/></svg>
  </div>
  <div class="abs feat-title" style="left:248px;top:1968px">Reflects Awareness</div>
  <p class="abs feat-copy" style="left:248px;top:2006px">Sed ut perspiciatis unde omnis iste natus error voluptatem accu santium</p>
  <div class="abs ring" style="left:110px;top:2103px">
    <svg width="56" height="56" viewBox="0 0 56 56" fill="none" stroke="#eb3d1f" stroke-width="2"><path d="M28 4 L48 12 V28 C48 40 38 48 28 52 C18 48 8 40 8 28 V12 Z"/><path d="M19 28 L26 35 L38 22"/></svg>
  </div>
  <div class="abs feat-title" style="left:248px;top:2114px">Safety</div>
  <p class="abs feat-copy" style="left:248px;top:2152px">Sed ut perspiciatis unde omnis iste natus error voluptatem accu santium</p>
  <div class="abs why-photo" role="img" aria-label="Surveyor in hard hat and hi-vis vest at a total station beside a tower crane"></div>
</section>

<section class="testimonials">
  <div class="abs testi-bg"></div>
  <div class="abs center eyebrow" style="top:2306px;font-size:21px">BRISK FRAMING</div>
  <h2 class="abs center title" style="top:2342px">TESTIMONIALS</h2>

  <div class="abs card" style="left:112px;top:2418px"><span class="mark">“</span><span class="stars">★★★★★</span><p>Sed ut perspiciatis unde omnis iste natus error sit voluptatem accusantium dolorem que laudantium, totam rem aperiam, eaq ue ipsa quae ab illo inventore veritatis et quasi arch ecto beatae vitae dicta sunt explicabo.Nemo enim ipsam voluptatem quia voluptas sit as pernatur aut odit aut fugit......</p></div>
  <div class="abs card" style="left:444px;top:2418px"><span class="mark">“</span><span class="stars">★★★★★</span><p>Sed ut perspiciatis unde omnis iste natus error sit voluptatem accusantium dolorem que laudantium, totam rem aperiam, eaq ue ipsa quae ab illo inventore veritatis et quasi arch ecto beatae vitae dicta sunt explicabo.Nemo enim ipsam voluptatem quia voluptas sit as pernatur aut odit aut fugit......</p></div>
  <div class="abs card" style="left:775px;top:2418px"><span class="mark">“</span><span class="stars">★★★★★</span><p>Sed ut perspiciatis unde omnis iste natus error sit voluptatem accusantium dolorem que laudantium, totam rem aperiam, eaq ue ipsa quae ab illo inventore veritatis et quasi arch ecto beatae vitae dicta sunt explicabo.Nemo enim ipsam voluptatem quia voluptas sit as pernatur aut odit aut fugit......</p></div>

  <div class="abs avatar" style="left:111px;top:2720px" role="img" aria-label="Client portrait"></div>
  <div class="abs author" style="left:192px;top:2738px">Maren Holt<span>Sed ut perspiciatis unde</span></div>
  <div class="abs avatar" style="left:443px;top:2720px" role="img" aria-label="Client portrait"></div>
  <div class="abs author" style="left:524px;top:2738px">Maren Holt<span>Sed ut perspiciatis unde</span></div>
  <div class="abs avatar" style="left:774px;top:2720px" role="img" aria-label="Client portrait"></div>
  <div class="abs author" style="left:855px;top:2738px">Maren Holt<span>Sed ut perspiciatis unde</span></div>
</section>

<section class="projects">
  <div class="abs center eyebrow" style="top:2896px;font-size:21px">BRISK FRAMING</div>
  <h2 class="abs center title" style="top:2932px">PAST PROJECTS</h2>
  <div class="abs proj" style="left:112px;top:3011px;width:645px;height:251px;background:linear-gradient(180deg,#5f86b8 0%,#c6a27a 55%,#e9a04a 75%,#2c2520 100%)" role="img" aria-label="Silhouettes of workers on steel framing at sunset"></div>
  <div class="abs proj-overlay" style="left:149px;top:3048px;font-size:27px;font-weight:600">Sed ut perspiciatis</div>
  <div class="abs proj-overlay" style="left:149px;top:3088px;font-size:15px;font-weight:500">Nemo enim ipsam voluptatem quia voluptas</div>
  <div class="abs proj" style="left:775px;top:3011px;width:315px;height:251px;background:linear-gradient(180deg,#b9c4cc,#d9cdb9 60%,#8a7560)" role="img" aria-label="Concrete frame building rising in front of a city skyline"></div>
  <div class="abs proj" style="left:112px;top:3280px;width:313px;height:250px;background:linear-gradient(160deg,#e6e6e6,#9c9a8a 50%,#4a6a3a)" role="img" aria-label="Engineer in a white hard hat reviewing a tablet over a site"></div>
  <div class="abs proj" style="left:444px;top:3280px;width:313px;height:250px;background:linear-gradient(180deg,#c9d6e2,#e6c07a 50%,#6c5a44)" role="img" aria-label="Surveyor at a tripod beside cranes in warm evening light"></div>
  <div class="abs proj" style="left:775px;top:3280px;width:315px;height:250px;background:linear-gradient(160deg,#8fb0d6,#e4dcd0 50%,#c96a2e)" role="img" aria-label="Two workers in orange vests pointing at a crane"></div>
</section>

<footer>
  <div class="abs footer"></div>
  <span class="abs fnav" style="left:356px">HOME</span>
  <span class="abs fnav" style="left:445px">SERVICES</span>
  <span class="abs fnav" style="left:563px">PROJECTS</span>
  <span class="abs fnav" style="left:685px">NEWS</span>
  <span class="abs fnav" style="left:777px">CONTACT</span>
  <div class="abs fline" style="top:3728px"></div>

  <h3 class="abs fhead" style="left:112px;top:3762px">CONTACT US</h3>
  <div class="abs field" style="left:112px;top:3818px;width:180px">First Name :</div>
  <div class="abs field" style="left:302px;top:3818px;width:180px">Last Name :</div>
  <div class="abs field" style="left:112px;top:3862px;width:180px">Email :</div>
  <div class="abs field" style="left:302px;top:3862px;width:180px">Phone :</div>
  <div class="abs field" style="left:112px;top:3906px;width:370px;height:54px">Message :</div>
  <div class="abs submit">SUBMIT</div>

  <h3 class="abs fhead" style="left:560px;top:3762px">ADDRESS</h3>
  <div class="abs ficon" style="left:551px;top:3818px"><svg width="16" height="20" viewBox="0 0 16 20"><path d="M8 1 C4 1 1 4 1 8 C1 13 8 19 8 19 C8 19 15 13 15 8 C15 4 12 1 8 1 Z" fill="none" stroke="#fff" stroke-width="2"/><circle cx="8" cy="8" r="2.5" fill="#fff"/></svg></div>
  <div class="abs finfo" style="left:610px;top:3818px">ADDRESS<span># Lorem Ipsum Dummy Lorem</span></div>
  <div class="abs ficon" style="left:551px;top:3880px"><svg width="18" height="18" viewBox="0 0 18 18"><path d="M4 1 L7 5 L5 7 C6 10 8 12 11 13 L13 11 L17 14 L15 17 C8 17 1 10 1 3 Z" fill="none" stroke="#fff" stroke-width="1.6"/></svg></div>
  <div class="abs finfo" style="left:610px;top:3880px">PHONE<span>555-014-2786</span></div>
  <div class="abs ficon" style="left:551px;top:3943px"><svg width="18" height="14" viewBox="0 0 18 14"><rect x="1" y="1" width="16" height="12" fill="#fff"/><path d="M1 1 L9 8 L17 1" fill="none" stroke="#eb3d1f" stroke-width="1.5"/></svg></div>
  <div class="abs finfo" style="left:610px;top:3943px">EMAIL<span>hello@briskframing.example</span></div>

  <div class="abs flogo">BRISK FRAMING</div>
  <span class="abs social" style="left:866px"></span>
  <span class="abs social" style="left:909px"></span>
  <span class="abs social" style="left:952px"></span>
  <span class="abs social" style="left:995px"></span>
  <span class="abs social" style="left:1038px"></span>

  <div class="abs fline" style="top:4030px"></div>
  <p class="abs center copyright">© Copyright 2022 Brisk Framing.All Rights Reserved</p>
</footer>
</body>
</html>
```